RK Bastone Construction Inc.

Design a new business card for our construction company
To be removed from current card:
Delete 25 years
Delete Tenant fit up Renovations section

```html
<!DOCTYPE html>
<html lang="en">
<head>
<meta charset="utf-8">
<title>RK Bastone Construction Inc. — Business Card</title>
<link rel="stylesheet" href="https://fonts.googleapis.com/css2?family=Arimo:wght@400;700&display=swap">
<style>
  :root {
    --purple: #4a2a6e;
    --teal: #1f7a6c;
    --ink: #2a2a2a;
    --card: #f7f7f8;
    --backdrop: #d9d9dc;
  }
  * { box-sizing: border-box; margin: 0; padding: 0; }
  html, body { width: 1200px; height: 800px; overflow: hidden; }
  body {
    background: var(--backdrop);
    font-family: "Arimo", Arial, sans-serif;
    display: flex;
    align-items: center;
    justify-content: center;
    gap: 40px;
  }
  .card {
    position: relative;
    width: 540px;
    height: 309px;
    background: var(--card);
    border-bottom: 3px solid var(--purple);
    box-shadow: 0 10px 24px rgba(0,0,0,0.18);
    overflow: hidden;
  }
  /* Front */
  .band {
    position: absolute; top: 0; left: 0; right: 0; height: 62px;
    background: var(--purple);
  }
  .band-accent {
    position: absolute; top: 0; left: 0; width: 110px; height: 100%;
    background: var(--teal);
    border-right: 2px solid var(--card);
  }
  .person-name {
    position: absolute; right: 24px; top: 20px;
    color: var(--teal); font-weight: 700; font-size: 17px;
  }
  .front .company-name {
    position: absolute; left: 118px; top: 72px;
    color: var(--purple); font-weight: 700; font-size: 17px;
    letter-spacing: 0.02em;
  }
  .address {
    position: absolute; left: 56px; top: 176px;
    font-size: 13px; line-height: 1.45; color: var(--ink);
  }
  .phones { margin-top: 14px; }
  .contact-line { display: flex; align-items: center; gap: 8px; }
  .contact-line svg { width: 11px; height: 11px; flex: none; }
  .online {
    position: absolute; left: 300px; top: 176px;
    font-size: 13px; line-height: 1.45; color: var(--ink);
  }
  /* Back */
  .back .identity {
    position: absolute; left: 48px; top: 112px;
  }
  .back .company-name {
    color: var(--purple); font-weight: 700; font-size: 27px;
    letter-spacing: 0.01em;
  }
  .tagline {
    margin-top: 22px;
    color: var(--purple); font-weight: 700; font-size: 17px;
    letter-spacing: 0.03em;
  }
  .tagline .divider { color: var(--teal); margin: 0 6px; }
</style>
</head>
<body>
  <section class="card front" aria-label="Business card front">
    <div class="band"><div class="band-accent"></div></div>
    <p class="person-name">Marco Bastone</p>
    <p class="company-name">RK Bastone Construction Inc.</p>

    <div class="address">
      <p>2215 Harlow Rd.</p>
      <p>Suite 100, Ottawa</p>
      <p>ON K2B7T4</p>
      <div class="phones">
        <p class="contact-line">
          <svg viewBox="0 0 12 12" aria-hidden="true"><path d="M3 1 L5 3.5 L4 5 Q5.5 7.5 7 8 L8.5 7 L11 9 L9.5 11 Q4 10.5 1 3 Z" fill="var(--purple)"/></svg>
          613-555-0142 ext.221
        </p>
        <p class="contact-line">
          <svg viewBox="0 0 12 12" aria-hidden="true"><rect x="3" y="0.5" width="6" height="11" rx="1" fill="none" stroke="var(--purple)" stroke-width="1.4"/></svg>
          613-555-0187
        </p>
      </div>
    </div>

    <div class="online">
      <p class="contact-line">
        <svg viewBox="0 0 12 12" aria-hidden="true"><rect x="0.5" y="2.5" width="11" height="7.5" fill="var(--purple)"/><path d="M0.5 2.5 L6 7 L11.5 2.5" fill="none" stroke="var(--card)" stroke-width="1"/></svg>
        marco@rkbastoneconst.ca
      </p>
      <p class="contact-line">
        <svg viewBox="0 0 12 12" aria-hidden="true"><circle cx="6" cy="6" r="5.5" fill="var(--purple)"/><ellipse cx="6" cy="6" rx="2.2" ry="5.5" fill="none" stroke="var(--card)" stroke-width="0.8"/></svg>
        www.rkbastoneconstruction.ca
      </p>
    </div>
  </section>

  <section class="card back" aria-label="Business card back">
    <div class="identity">
      <p class="company-name">RK Bastone Construction Inc.</p>
      <p class="tagline">Office<span class="divider">|</span>Retail<span class="divider">|</span>Institutional</p>
    </div>
  </section>
</body>
</html>
```